Thai Menu Design Project

We need a new menu design for a Thai restaurant in Fort Worth, Texas. We are a family-owned and really proud about our food and our service. We want the menu to feel healthy, modern, delicious, artistic Thai, and friendly. The colors we used in our restaurant are maroon, burgundy, black, white, gold and pale yellow.

Please look at our website www.brindlewokery.com
for the reference of the menus and the photos we use.

The menu can be in any number of pages (the fewer the better though) The size of the paper is US letter.
Updates

Update:

- We don't put the photos of the food in the menu pages anymore, instead, we like to put the photos of the herbs and their benefits (found in the file 'herb benefits') on the menu pages instead.

- the paper size is US letter.

- we don't have specific numbers of pages but the fewer the better

Thank you!

I added logos and background photo again in case the previous files did not work. Thanks!

Target Market(s)

Trendy socialized people from 20-30s,couples of all ages from 20s-60s,and families.

Industry/Entity Type

Restaurant

Requirements
Must have
• We want the menu to feel healthy, modern, delicious, artistic, Thai, and friendly.

We like to keep the colors maroon, burgundy, black, gold, pale yellow, and off white.

We like to put the photos of the herbs and their benefits (available in the file called 'herb benefits') randomly in the menu pages.

*Please use the photos available in the file called 'herb benefits' along with its details somewhere in the pages. You can change the photo of each herb to the ones you find more fitting from the internet.

Nice to have
• If we can add the wallpaper pattern in our menu it will be great. It can be used in anyway.

```html
<!DOCTYPE html>
<html lang="en">
<head>
<meta charset="utf-8">
<title>Brindle Wokery – Appetizers Menu</title>
<link rel="stylesheet" href="https://fonts.googleapis.com/css2?family=Open+Sans:wght@400;700&display=swap">
<style>
  :root {
    --stage: #ffffff;
    --maroon: #7a1e22;
    --maroon-deep: #5e1418;
    --gold: #c9962e;
    --gold-light: #e6b24e;
    --gold-text: #dba653;
    --tab: #dcc6a2;
    --tab-text: #6b4a2a;
    --ink: #2a1a0e;
  }
  * { box-sizing: border-box; margin: 0; padding: 0; }
  html, body {
    width: 1200px; height: 1001px; overflow: hidden;
    background: var(--stage);
    font-family: "Open Sans", Arial, sans-serif;
  }
  .menu-page {
    position: absolute; left: 229px; top: 20px;
    width: 742px; height: 960px;
    background: var(--maroon);
    border-right: 14px solid var(--gold);
    overflow: hidden;
  }
  .pattern-band {
    position: absolute; left: 0; top: 0; width: 100%; height: 46px;
    background: linear-gradient(180deg, #9a3b22 0%, #b5712c 55%, var(--maroon) 100%);
  }
  .section-tab {
    position: absolute; left: 0; top: 12px;
    width: 180px; height: 38px;
  }
  .section-tab svg { position: absolute; inset: 0; }
  .section-tab h1 {
    position: relative; font-size: 23px; font-weight: 700; letter-spacing: 0.5px;
    color: var(--tab-text); line-height: 38px; padding-left: 24px;
  }
  .item-columns {
    position: absolute; left: 28px; top: 66px; right: 24px;
    display: flex; gap: 34px;
  }
  .item-column { flex: 1; display: flex; flex-direction: column; gap: 12px; }
  .menu-item { color: var(--gold-text); }
  .item-head {
    display: flex; justify-content: space-between;
    font-size: 14.5px; font-weight: 700; color: var(--gold-light);
  }
  .item-desc { font-size: 13.5px; line-height: 1.3; }
  .herb-panel {
    position: absolute; left: 0; top: 676px; width: 100%; height: 242px;
    background: var(--gold);
    display: flex; gap: 14px; padding: 10px 18px 10px 28px;
  }
  .herb-photo {
    flex: 0 0 266px; height: 222px;
    background: radial-gradient(ellipse at 45% 55%, #e8cfa3 0%, #a97a4a 40%, #4a2c18 100%);
  }
  .herb-text { font-size: 15px; line-height: 1.36; color: var(--ink); padding-top: 6px; }
  .herb-text strong { font-weight: 700; }
  .page-footer {
    position: absolute; left: 0; bottom: 14px; width: 100%;
    text-align: center; font-size: 11.5px; font-weight: 700; color: var(--gold-light);
  }
</style>
</head>
<body>
<main class="menu-page">
  <div class="pattern-band" role="img" aria-label="Ornamental Thai wallpaper pattern band"></div>
  <div class="section-tab">
    <svg width="180" height="38" viewBox="0 0 180 38"><polygon points="0,0 162,0 180,19 162,38 0,38" fill="var(--tab)"/></svg>
    <h1>APPETIZERS</h1>
  </div>

  <div class="item-columns">
    <div class="item-column">
      <div class="menu-item"><div class="item-head"><span>Chicken Satay (6)</span><span>9</span></div><p class="item-desc">Marinated chicken on skewers served with our famous peanut sauce and cucumber salad</p></div>
      <div class="menu-item"><div class="item-head"><span>Coconut Shrimp (6)New!</span><span>8</span></div><p class="item-desc">Served with sweet spicy dipping sauce</p></div>
      <div class="menu-item"><div class="item-head"><span>Brindle Wokery Sampler</span><span>14</span></div><p class="item-desc">2 Chicken Satay, 2 Golden Shrimp, 2 Pot Stickers, 2 Crab Rangoon, and 2 Crispy Spring Roll</p></div>
      <div class="menu-item"><div class="item-head"><span>Three Musketeers (V)New!</span><span>9</span></div><p class="item-desc">2 Awesome Taro, 2 Sweet Corn Cakes, and 2 Crispy Tofu. All Vegetarians!</p></div>
      <div class="menu-item"><div class="item-head"><span>Fried Calamari</span><span>8</span></div><p class="item-desc">Battered calamari served with plum sauce</p></div>
      <div class="menu-item"><div class="item-head"><span>Crab Rangoon (6)</span><span>7.5</span></div><p class="item-desc">Crab with cream cheese in crispy wonton skin</p></div>
      <div class="menu-item"><div class="item-head"><span>Fish Cake (6)New!</span><span>8</span></div><p class="item-desc">Thai-style spicy fishcake served with cucumber vinaigrette</p></div>
      <div class="menu-item"><div class="item-head"><span>Thai Beef Jerky</span><span>9</span></div><p class="item-desc">Sliced fried beef marinated with Thai seasoning, served with flavorful dipping sauce</p></div>
      <div class="menu-item"><div class="item-head"><span>Sweet Corn cake (5)(V)</span><span>7.5</span></div><p class="item-desc">Seasoned sweet corn battered and deep-fried served with sweet sauce</p></div>
      <div class="menu-item"><div class="item-head"><span>Edamame(V)</span><span>5</span></div><p class="item-desc">Steamed salted soybeans</p></div>
    </div>
    <div class="item-column">
      <div class="menu-item"><div class="item-head"><span>Chicken or Tofu Lettuce Wrap (V)</span><span>9</span></div><p class="item-desc">Minced chicken or tofu, water chestnuts, mushrooms, scallions, crispy noodles and cool lettucecups with spicy lime sauce</p></div>
      <div class="menu-item"><div class="item-head"><span>Crispy Soft Shell Crabs (2)</span><span>8</span></div><p class="item-desc">Soft shell crabs fried to a light crisp served with sweet and spicy sauce</p></div>
      <div class="menu-item"><div class="item-head"><span>Pot Stickers (8)</span><span>7.5</span></div><p class="item-desc">Pork and cabbage dumplings served steamed or fried</p></div>
      <div class="menu-item"><div class="item-head"><span>Mixed Vegetable Tempura (V)</span><span>9</span></div><p class="item-desc">Breaded green beans, eggplant, carrot, and broccoli served with Thai ginger sauce</p></div>
      <div class="menu-item"><div class="item-head"><span>Cucumber Salad (V)</span><span>5</span></div><p class="item-desc">Sliced cucumber in sweet vinaigrette</p></div>
      <div class="menu-item"><div class="item-head"><span>Crispy Spring Rolls (5)</span><span>7.50</span></div><p class="item-desc">Pork, carrot, cabbage, and noodles in Thai spring roll wrapper<br>Vegetarian Spring Rolls (5) (V)</p></div>
      <div class="menu-item"><div class="item-head"><span>Egg Roll (1)</span><span>1.65</span></div><p class="item-desc">Crispy eggroll stuffed with seasoned pork and cabbage<br>Vegetarian Egg Roll (V)</p></div>
      <div class="menu-item"><div class="item-head"><span>Summer Rolls (2) (V)</span><span>3</span></div><p class="item-desc">Romaine lettuce, vermicelli, cilantro, carrot, and red cabbage in rice wrapper served with peanut sauce<br>For Tofu or Shrimp add 1</p></div>
    </div>
  </div>

  <section class="herb-panel">
    <div class="herb-photo" role="img" aria-label="Photo of fresh galangal root on a wooden table"></div>
    <p class="herb-text"><strong>Galangal |</strong> Commonly known as ‘Siamese ginger’, the name galangal is derived form the Chinese word for ginger. Galangal contains anti-inflammatory properties which is beneficial in treatment of arthritis and rheumatoid arthritis. Galangal contains a host of anti-oxidants that helps to minimise the damage caused by free radicals and other toxins in the body. To improve blood circulation in the body, include galangal in your diet.</p>
  </section>

  <p class="page-footer">(V) for Vegetarian. No substitute please. Up to 5 credit card per check, thank you.</p>
</main>
</body>
</html>
```